Business card required for IT Consultancy Business - Tealbrook Consulting.
Company provides the whole nine yards of services across IT Architecture, design and execution.
Basically we provide consulting services to help businesses make sure their technology is enabling their business strategy.
Design for front and back required.
We would like the front of the card to inlcude:
Name
Title
Mobile number
email address
www.tbkc.com.au
Company logos attached.
Thank you
Industry/Entity Type
Business
Contact Information for Business Card
Name
Title
Mobile number
email address
www.tbkc.com.au
Look and feel
Each slider illustrates characteristics of the customer's brand and the style your logo design should communicate.

```html
<!DOCTYPE html>
<html lang="en">
<head>
<meta charset="utf-8">
<title>Tealbrook Consulting – Business Card</title>
<link rel="stylesheet" href="https://fonts.googleapis.com/css2?family=Roboto:wght@400;500;700&family=Roboto+Condensed:wght@500;700&display=swap">
<style>
  :root {
    --backdrop: #262626;
    --card: #f1f1f1;
    --brand-blue: #1473bb;
    --brand-orange: #f15a24;
    --white: #ffffff;
    --muted: #555555;
  }
  * { box-sizing: border-box; margin: 0; padding: 0; }
  html, body {
    width: 1200px; height: 960px; overflow: hidden;
    background: var(--backdrop);
    font-family: "Roboto", Arial, sans-serif;
  }
  .card {
    position: absolute;
    width: 600px; height: 343px;
    background: var(--card);
    box-shadow: 0 3px 8px rgba(0,0,0,.5);
    overflow: hidden;
  }
  .card--front { left: 314px; top: 113px; }
  .card--back  { left: 311px; top: 472px; }

  .wordmark {
    position: absolute;
    display: flex; align-items: center; gap: 12px;
    color: var(--brand-blue);
    font-family: "Roboto", Arial, sans-serif;
    font-weight: 700;
    white-space: nowrap;
  }
  .wordmark__dot {
    border-radius: 50%;
    background: var(--brand-orange);
    flex: none;
  }
  .card--front .wordmark {
    left: 0; right: 0; top: 78px; justify-content: center; font-size: 30px;
  }
  .card--front .wordmark__dot { width: 26px; height: 26px; }

  .band { position: absolute; left: 0; top: 0; width: 600px; height: 343px; }

  .holder {
    position: absolute; left: 58px; top: 260px; color: var(--white);
  }
  .holder__name {
    font-family: "Roboto Condensed", Arial, sans-serif;
    font-weight: 700; font-size: 21px; letter-spacing: .2px;
  }
  .holder__title {
    font-family: "Roboto Condensed", Arial, sans-serif;
    font-weight: 500; font-size: 15px; margin-top: 3px;
  }

  .contacts {
    position: absolute; left: 368px; top: 254px;
    list-style: none; color: var(--white); font-size: 14px;
  }
  .contacts li {
    display: flex; align-items: center; gap: 9px; height: 19px;
  }
  .contacts svg { width: 13px; height: 13px; flex: none; }

  .card--back .wordmark {
    left: 0; right: 0; top: 140px; justify-content: center; font-size: 40px;
  }
  .card--back .wordmark__dot { width: 34px; height: 34px; }
  .back__web {
    position: absolute; left: 0; right: 0; top: 300px;
    text-align: center; color: var(--muted);
    font-size: 14px; letter-spacing: 7px;
  }
</style>
</head>
<body>
  <section class="card card--front">
    <div class="wordmark"><span class="wordmark__dot"></span>Tealbrook Consulting</div>

    <svg class="band" viewBox="0 0 600 343" aria-hidden="true">
      <polygon points="0,219 318,219 303,234 0,234" fill="var(--brand-orange)"/>
      <polygon points="337,202 600,202 600,343 0,343 0,236 306,236" fill="var(--brand-blue)"/>
    </svg>

    <div class="holder">
      <div class="holder__name">DANIEL REYES</div>
      <div class="holder__title">CEO/FOUNDER</div>
    </div>

    <ul class="contacts">
      <li>
        <svg viewBox="0 0 13 13"><rect x="3" y="0.5" width="7" height="12" rx="1.2" fill="none" stroke="#fff" stroke-width="1.3"/><circle cx="6.5" cy="10.5" r=".8" fill="#fff"/></svg>
        555 214 7830
      </li>
      <li>
        <svg viewBox="0 0 13 13"><rect x="1" y="3" width="11" height="7.5" fill="#fff"/><polyline points="1,3 6.5,7.5 12,3" fill="none" stroke="#1473bb" stroke-width="1"/></svg>
        hello@tbkc.com.au
      </li>
      <li>
        <svg viewBox="0 0 13 13"><circle cx="6.5" cy="6.5" r="5.8" fill="#fff"/><path d="M4 3.5c1.5.5 2 1.5 1 2.5s.5 2 1.5 2.5M8 2.2c-.5 1.3.8 1.8 1.8 1.5M9 9.5c.5-1 1.5-1 2-.5" fill="none" stroke="#1473bb" stroke-width="1"/></svg>
        www.tbkc.com.au
      </li>
    </ul>
  </section>

  <section class="card card--back">
    <div class="wordmark"><span class="wordmark__dot"></span>Tealbrook Consulting</div>
    <div class="back__web">www.tbkc.com.au</div>
  </section>
</body>
</html>
```